New Update: I am changing the title of the book and the back cover text. Title was too long before. Same style as before.
New Title: Under the Quiet Sky
New Subtitle: A Gardener’s Notes on Patience (italics on front cover)

Back cover text:
Under the Quiet Sky: A Gardener’s Notes on Patience offers clear, compassionate guidance for those recovering from total loss. Drawing from his experience as a Brennick Flood survivor, Tobias Quellhorst shares practical advice on insurance, rebuilding, and emotional healing, along with lessons in strength and community. This is not a book about tragedy; it’s about perseverance and renewal. Under the Quiet Sky is a trusted companion for anyone rebuilding life, home, and hope after disaster.

Font styles to use
Serif

Colors
EB3D1F
EC4F4E
F09395
F8D3D4
FCEDEE

Requirements
Should not have
• No pictures or anything related to fire on the cover.

```html
<!DOCTYPE html>
<html lang="en">
<head>
<meta charset="utf-8">
<title>Under the Quiet Sky – Cover Wrap</title>
<link href="https://fonts.googleapis.com/css2?family=Anton&family=Cinzel:wght@600;700&family=Crimson+Text:ital,wght@0,400;1,400&family=Playfair+Display:ital,wght@1,700&display=swap" rel="stylesheet">
<style>
  :root {
    --backdrop: #dcdbd8;
    --vermilion: #eb3d1f;
    --coral: #ec4f4e;
    --rose: #f09395;
    --blush: #f8d3d4;
    --cream: #fcedee;
    --edge-shade: #8e2414;
    --spine-shade: #b02e17;
    --photo-tone: #a0463a;
  }
  * { margin: 0; padding: 0; box-sizing: border-box; }
  html, body { width: 1200px; height: 900px; overflow: hidden; background: var(--backdrop); }
  .cover-wrap {
    position: absolute; left: 35px; top: 45px;
    width: 1130px; height: 810px; display: flex;
    box-shadow: 0 10px 30px rgba(0,0,0,.25);
  }
  .back-cover, .front-cover {
    position: relative; width: 540px; height: 810px; overflow: hidden;
    background: radial-gradient(ellipse at 55% 45%, var(--coral) 0%, var(--vermilion) 45%, var(--edge-shade) 100%);
  }
  .spine {
    width: 50px; height: 810px; position: relative;
    background: linear-gradient(90deg, var(--spine-shade), var(--vermilion) 50%, var(--spine-shade));
  }
  .spine-title {
    position: absolute; left: 50%; top: 50%;
    transform: translate(-50%, -50%) rotate(90deg);
    white-space: nowrap; font-family: "Crimson Text", serif;
    font-size: 20px; letter-spacing: 1.5px; color: var(--cream); text-transform: uppercase;
  }
  .spine-title .accent { color: var(--blush); }

  /* Front cover */
  .rule { position: absolute; left: 40px; right: 40px; height: 2px; background: var(--rose); }
  .front-cover .rule.top { top: 40px; }
  .front-cover .rule.mid { top: 650px; }
  .rope-art { position: absolute; left: 385px; top: 300px; z-index: 0; }
  .title-lockup { position: absolute; left: 0; right: 0; top: 75px; text-align: center; z-index: 1; }
  .title-small {
    font-family: "Cinzel", serif; font-weight: 700; color: var(--cream);
    font-size: 44px; letter-spacing: 3px; line-height: 1;
  }
  .title-large {
    font-family: "Anton", sans-serif; font-size: 132px; line-height: 1;
    letter-spacing: 2px; text-transform: uppercase;
  }
  .title-large.accent { color: var(--blush); margin-top: 10px; }
  .title-large.light { color: var(--cream); }
  .subtitle-script {
    position: absolute; left: 0; right: 0; top: 560px; text-align: center;
    font-family: "Playfair Display", serif; font-style: italic; font-weight: 700;
    font-size: 34px; color: var(--cream);
  }
  .tagline {
    position: absolute; left: 0; right: 0; top: 680px; text-align: center;
    font-family: "Crimson Text", serif; font-size: 24px; line-height: 1.25; color: var(--cream);
  }

  /* Back cover */
  .back-heading {
    position: absolute; left: 0; right: 0; top: 55px; text-align: center;
    font-family: "Cinzel", serif; font-weight: 700; color: var(--blush);
    font-size: 40px; line-height: 1.15; letter-spacing: 1px;
  }
  .back-blurb {
    position: absolute; left: 50px; right: 50px; top: 170px; text-align: center;
    font-family: "Crimson Text", serif; font-size: 20px; line-height: 1.35; color: var(--cream);
  }
  .back-quote {
    position: absolute; left: 50px; right: 50px; top: 420px; text-align: center;
    font-family: "Crimson Text", serif; font-style: italic; font-size: 20px;
    line-height: 1.35; color: var(--blush);
  }
  .author-band { position: absolute; left: 0; top: 600px; width: 540px; height: 120px; }
  .author-name {
    position: absolute; left: 0; right: 0; top: 735px; text-align: center;
    font-family: "Anton", sans-serif; font-size: 36px; letter-spacing: 2px; color: var(--blush);
  }
</style>
</head>
<body>
<div class="cover-wrap">

  <section class="back-cover">
    <h2 class="back-heading">UNDER THE<br>QUIET SKY</h2>
    <p class="back-blurb">Under the Quiet Sky: A Gardener’s Notes on Patience offers clear, compassionate guidance for those recovering from total loss. Drawing from his experience as a Brennick Flood survivor, Tobias Quellhorst shares practical advice on insurance, rebuilding, and emotional healing, along with lessons in strength and community.</p>
    <p class="back-quote">This is not a book about tragedy; it’s about perseverance and renewal. Under the Quiet Sky is a trusted companion for anyone rebuilding life, home, and hope after disaster.</p>
    <svg class="author-band" viewBox="0 0 540 120">
      <line x1="0" y1="14" x2="540" y2="14" stroke="var(--rose)" stroke-width="2"/>
      <rect x="0" y="44" width="540" height="32" fill="var(--cream)"/>
      <line x1="0" y1="106" x2="540" y2="106" stroke="var(--rose)" stroke-width="2"/>
      <circle cx="330" cy="60" r="58" fill="var(--cream)" stroke="var(--rose)" stroke-width="3"/>
      <circle cx="330" cy="60" r="54" fill="var(--photo-tone)" role="img" aria-label="Portrait photograph of the author"/>
    </svg>
    <div class="author-name">TOBIAS QUELLHORST</div>
  </section>

  <aside class="spine">
    <div class="spine-title">Under the Quiet Sky: <span class="accent">A Gardener’s Notes on Patience</span></div>
  </aside>

  <section class="front-cover">
    <div class="rule top"></div>
    <svg class="rope-art" width="130" height="230" viewBox="0 0 130 230" role="img" aria-label="Knotted rope illustration with tassel ends">
      <defs>
        <linearGradient id="ropeTone" x1="0" y1="0" x2="1" y2="1">
          <stop offset="0" stop-color="#f8d3d4" stop-opacity=".45"/>
          <stop offset="1" stop-color="#f09395" stop-opacity=".3"/>
        </linearGradient>
      </defs>
      <rect x="0" y="0" width="130" height="230" rx="65" fill="url(#ropeTone)"/>
    </svg>
    <div class="title-lockup">
      <div class="title-small">UNDER THE</div>
      <div class="title-large accent">QUIET</div>
      <div class="title-large light">SKY</div>
    </div>
    <div class="subtitle-script">A Gardener’s Notes on Patience</div>
    <div class="rule mid"></div>
    <p class="tagline">A Journey Through Loss, Recovery,<br>and Rebuilding</p>
  </section>

</div>
</body>
</html>
```